Tall Ferns "Quiet Lane" New Single Cover

Create cover artwork for the band Tall Ferns' new single "Quiet Lane" being released early 2020. Style, font and graphics to be consistent with band's previous releases and overall brand identity. Visit www.tallfernsband.example and our Tunelane page https://music.example.net/artist/7KqPzTw2RxLmVbN4cYdJhE?si=GhTrWpLmZxQvBnKsYdFcRa to view our previous releases and overall brand identity. Some examples attached as well. We are looking for someone to work with on future projects as well.

Lyrics are here: https://files.example.org/document/d/4PxLm8TrQw2ZvKn7YbHcJdRfGsWe5AuNiOpXlMkBtCvE/edit

Music is here: https://audioshare.example.com/tallferns/quiet-lane/s-kdmwp

Font styles to use
Sans Serif

Colors

Designer to choose colors to be used in the design.

Requirements
Must have
• Must be consistent with current brand identity and with prior album / single art.

```html
<!DOCTYPE html>
<html lang="en">
<head>
<meta charset="utf-8">
<title>Tall Ferns – Quiet Lane</title>
<link rel="stylesheet" href="https://fonts.googleapis.com/css2?family=Montserrat:wght@400;800&display=swap">
<style>
  :root {
    --backdrop: #5e5e5e;
    --cover-teal: #17a5ab;
    --sun-orange: #f5ab1f;
    --title-navy: #1f2d5c;
    --band-white: #ffffff;
  }
  html, body {
    margin: 0;
    padding: 0;
    overflow: hidden;
  }
  body {
    width: 1200px;
    height: 793px;
    background: var(--backdrop);
    position: relative;
    font-family: "Montserrat", Arial, sans-serif;
  }
  .cover {
    position: absolute;
    left: 271px;
    top: 66px;
    width: 660px;
    height: 660px;
    background: var(--cover-teal);
  }
  .smile-grid {
    position: absolute;
    left: 85px;
    top: 40px;
    width: 490px;
    height: 493px;
    background: radial-gradient(circle at 50% 50%,
      rgba(245, 171, 31, 0.85) 0%,
      rgba(245, 171, 31, 0.45) 30%,
      rgba(245, 171, 31, 0.22) 100%);
  }
  .title-line {
    position: absolute;
    left: 0;
    right: 0;
    top: 548px;
    display: flex;
    justify-content: center;
    align-items: center;
    gap: 14px;
  }
  .single-word {
    font-weight: 800;
    font-size: 70px;
    line-height: 1;
    color: var(--title-navy);
    letter-spacing: 0;
  }
  .band-name {
    display: flex;
    flex-direction: column;
    align-items: center;
    color: var(--band-white);
    font-weight: 400;
    font-size: 17px;
    line-height: 1.2;
    letter-spacing: 0.14em;
  }
</style>
</head>
<body>
  <main class="cover">
    <div class="smile-grid" role="img" aria-label="Grid of twenty-five orange outlined smiling circles, the centre one filled orange with the band emblem"></div>
    <h1 class="title-line">
      <span class="single-word">QUIET</span>
      <span class="band-name"><span>TALL</span><span>FERNS</span></span>
      <span class="single-word">LANE</span>
    </h1>
  </main>
</body>
</html>
```